Wandtattoo Wandspruch Küche - Preisgeld + Umsatzbeteiligung
Zielgruppe
Zielgruppe sind alle, die sich Wandtattoos aufkleben. Hier speziell für die Küche.
Alter also etwa zwischen 20 und 60.
Eher etwas jünger.
Bei den älteren eher weiblicher.
Aufgabenstellung
Wir betreiben einen Online-Shop www.molvix.de und verkaufen bzw. stellen her: Wandtattoos und kreative Produkte für die Wandgestaltung.
Wir möchten nun unser Sortiment an hochwertigen Wandtattoos Wandsprüchen erweitern. Diese sollen online in unserem Shop und per Katalog bei Wiederverkäufern angeboten und verkauft werden.
Wir suchen wirklich eine große Anzahl an Wandsprüchen und hoffen, dass sie sich rege beteiligen. Wir würden nicht nur das Gewinner-Design in unser Sortiment aufnehmen, sondern alles, was gefällt und Käufer finden würde.
Das Preisgeld wird auf jeden Fall vergeben. Der Gewinner hier erhält ganz sicher das Preisgeld von 200,- Euro und eine zusätzliche Umsatzbeteiligung. Die Höhe richtet sich nach der verkauften Größe des Wandtattoos.
Die Umsatzbeteiligung erhält sonst natürlich jeder Designer, der uns Designs zur Verfügung stellt. Einzelheiten dazu finden Sie im Link unten bzw. auf unserer Homepage unter www.molvix.de.
Nun zu den Anforderungen:
Wir suchen Wandtexte, Wandsprüche, Wandtattoos speziell für die Küche.
Ob nun Rezepte oder Weisheiten. Witzig oder edel. Verspielt oder schlicht. Es soll für jeden Geschmack etwas dabei sein.
Das Gewinner-Design sollte schon etwas spezielles bieten. Ein besonderes Design oder ein besonders witziger Spruch.

```html
<!DOCTYPE html>
<html lang="de">
<head>
<meta charset="utf-8">
<title>Wandspruch Küche – Geschmack</title>
<link rel="stylesheet" href="https://fonts.googleapis.com/css2?family=Arimo:wght@400;700&family=Pinyon+Script&display=swap">
<style>
  :root {
    --wall: #545454;
    --decal: #ffffff;
  }
  html, body {
    margin: 0;
    padding: 0;
    overflow: hidden;
  }
  .wall-quote {
    position: relative;
    width: 1200px;
    height: 647px;
    background: var(--wall);
    color: var(--decal);
    overflow: hidden;
  }
  .quote-line {
    position: absolute;
    left: 0;
    width: 100%;
    margin: 0;
    text-align: center;
    font-family: "Arimo", Arial, sans-serif;
    font-weight: 700;
    font-size: 47px;
    line-height: 1;
    white-space: nowrap;
  }
  .quote-line--intro { top: 102px; left: -3px; }
  .quote-line--outro { top: 401px; left: 1px; }
  .quote-keyword {
    position: absolute;
    top: 176px;
    left: 0;
    width: 100%;
    margin: 0;
    text-align: center;
    font-family: "Pinyon Script", cursive;
    font-weight: 400;
    font-size: 150px;
    line-height: 1;
    white-space: nowrap;
    padding-right: 60px;
    box-sizing: border-box;
  }
  .quote-author {
    position: absolute;
    top: 494px;
    left: 428px;
    margin: 0;
    font-family: "Arimo", Arial, sans-serif;
    font-weight: 400;
    font-size: 28px;
    line-height: 1;
    white-space: nowrap;
  }
</style>
</head>
<body>
  <main class="wall-quote">
    <p class="quote-line quote-line--intro">Ich habe einen ganz einfachen</p>
    <p class="quote-keyword">Geschmack</p>
    <p class="quote-line quote-line--outro">ich bin immer mit dem Besten zufrieden.</p>
    <p class="quote-author">Edgar Lindholm</p>
  </main>
</body>
</html>
```